Fresh pet feed direct from manufacturer to door step. Quality and Freshness un-surpassed in Industr

Need Business Card Design; leading into many other projects, for New Franchised Business Opportunity providing home delivery of fresh dog and cat feed (no emphasis needed for cat) direct from manufacturing facility. (no middle men or distributors) Food is Farm to Factory fresh. Our trademarked tagline is "Quality is our MAIN Ingredient ! "
Updates

Please take note of other contest for Chirplane Cover and Profile Pic's

Target Market(s)

Dog and Cat owners

Industry/Entity Type

Pet

Contact Information for Business Card

Name, address, local phone, national 800 number, website, email address

Other font styles liked:
• follow that from logo

Requirements
Must have
• Our feed is made in Texas with ingredients sourced from local farms. We want to lean heavy on the Made in West Texas , ranch theme but that has a 'black label', 'vantrel', 'premium', 'high-end' look and feel
Nice to have
• maybe have an offer on card? 20% off with promo code "x" etc.. ?? just a thought...

```html
<!DOCTYPE html>
<html lang="en">
<head>
<meta charset="utf-8">
<title>Hollis Premium – Business Card</title>
<link href="https://fonts.googleapis.com/css2?family=Arimo:wght@400;500&family=Tinos:wght@400;700&display=swap" rel="stylesheet">
<style>
  :root {
    --ink: #221a26;
    --ink-soft: #3a3040;
    --paper: #f7f7f5;
    --gold: #e2b72e;
    --gold-deep: #b98f1a;
    --text-dark: #2e2a2e;
    --stage: #d9d6d0;
  }
  html, body {
    margin: 0;
    width: 1200px;
    height: 885px;
    overflow: hidden;
    background: var(--stage);
  }
  .canvas {
    position: relative;
    width: 1200px;
    height: 885px;
  }
  .card {
    position: absolute;
    left: 150px;
    top: 185px;
    width: 900px;
    height: 514px;
    background: var(--ink);
    box-shadow: 0 10px 30px rgba(0,0,0,.25);
    overflow: hidden;
  }
  .card-shapes {
    position: absolute;
    inset: 0;
  }
  .brand {
    position: absolute;
    left: 70px;
    top: 110px;
    width: 300px;
    display: flex;
    align-items: center;
    gap: 14px;
  }
  .brand-dot {
    width: 30px;
    height: 30px;
    border-radius: 50%;
    background: var(--ink);
    flex: none;
  }
  .brand-name {
    font-family: "Tinos", serif;
    font-weight: 700;
    font-size: 40px;
    line-height: 1.05;
    color: var(--ink);
    letter-spacing: 1px;
  }
  .person {
    position: absolute;
    left: 250px;
    top: 282px;
    display: flex;
    align-items: baseline;
    gap: 14px;
    color: #fff;
    font-family: "Arimo", sans-serif;
  }
  .person-name { font-size: 30px; }
  .person-role {
    font-size: 17px;
    padding-left: 14px;
    border-left: 1px solid rgba(255,255,255,.7);
  }
  .contact {
    position: absolute;
    font-family: "Tinos", serif;
    font-size: 21px;
    color: var(--text-dark);
    list-style: none;
    margin: 0;
    padding: 0;
  }
  .contact li {
    display: flex;
    align-items: flex-start;
    gap: 12px;
    line-height: 27px;
  }
  .contact-address { left: 370px; top: 378px; }
  .contact-lines { left: 660px; top: 378px; }
  .icon {
    width: 18px;
    height: 18px;
    margin-top: 5px;
    background: var(--gold);
    flex: none;
  }
  .icon svg { display: block; width: 18px; height: 18px; }
</style>
</head>
<body>
<main class="canvas">
  <section class="card" aria-label="Business card">
    <svg class="card-shapes" viewBox="0 0 900 514" aria-hidden="true">
      <path class="panel-brand" d="M0,0 H480 C440,160 330,250 0,262 Z" fill="var(--paper)"/>
      <path d="M480,0 C440,160 330,250 0,262" fill="none" stroke="var(--gold)" stroke-width="3"/>
      <path class="panel-contact" d="M220,514 C260,400 360,340 900,336 V514 Z" fill="var(--paper)"/>
      <path d="M220,514 C260,400 360,340 900,336" fill="none" stroke="var(--gold)" stroke-width="3"/>
    </svg>

    <div class="brand">
      <span class="brand-dot"></span>
      <span class="brand-name">HOLLIS<br>PREMIUM</span>
    </div>

    <div class="person">
      <span class="person-name">Employee Name</span>
      <span class="person-role">Managing Director</span>
    </div>

    <ul class="contact contact-address">
      <li>
        <span class="icon"><svg viewBox="0 0 18 18"><path d="M9 3a4 4 0 0 0-4 4c0 3 4 8 4 8s4-5 4-8a4 4 0 0 0-4-4zm0 5.5a1.5 1.5 0 1 1 0-3 1.5 1.5 0 0 1 0 3z" fill="var(--ink)"/></svg></span>
        <span>Your Adress Inc 2nd Lane<br>Ave Alder, TX 00000</span>
      </li>
      <li>
        <span class="icon"><svg viewBox="0 0 18 18"><circle cx="9" cy="9" r="5" fill="none" stroke="var(--ink)" stroke-width="1.4"/><path d="M4 9h10M9 4c-2.5 3-2.5 7 0 10M9 4c2.5 3 2.5 7 0 10" fill="none" stroke="var(--ink)" stroke-width="1.2"/></svg></span>
        <span>www.yourwebsite.com</span>
      </li>
    </ul>

    <ul class="contact contact-lines">
      <li>
        <span class="icon"><svg viewBox="0 0 18 18"><rect x="6" y="3" width="6" height="12" rx="1" fill="none" stroke="var(--ink)" stroke-width="1.4"/><circle cx="9" cy="12.5" r=".9" fill="var(--ink)"/></svg></span>
        <span>xxx xxx xxxx</span>
      </li>
      <li>
        <span class="icon"><svg viewBox="0 0 18 18"><path d="M5 3.5l2.5 2.5-1.3 1.8c.9 1.8 2.2 3.1 4 4l1.8-1.3 2.5 2.5-1.5 1.8C8.5 14.5 3.5 9.5 3.2 5z" fill="var(--ink)"/></svg></span>
        <span>(800) xxx xxxx</span>
      </li>
      <li>
        <span class="icon"><svg viewBox="0 0 18 18"><rect x="3.5" y="5" width="11" height="8" fill="none" stroke="var(--ink)" stroke-width="1.4"/><path d="M3.5 5l5.5 4.5L14.5 5" fill="none" stroke="var(--ink)" stroke-width="1.4"/></svg></span>
        <span>info@youremail.com</span>
      </li>
    </ul>
  </section>
</main>
</body>
</html>
```